New Flyer Design Project

We need a flyer for our upcoming Rising Builders Summit.

5th Annual Rising Builders Summit
by the Bureau for Advancement in Public Works (B-AdPW)
Theme: Stand Tall
Date: January 24, 2020
Location: Harborview Lodge Hotel and Conference Center, San Marcos, TX
#StandTall

This is event is put together by B-AdPW's Rising Builders Ring of Merit. I have a logo for the Ring of Merit, but not something that indicates it's the Rising Builders Ring.

More about the Forum (please don't include on the flyer): This Forum provides a venue to openly discuss issues affecting women in our industry and ideas and strategies to address those issues.

Architecture, Construction and Engineering are all struggling with a tremendous shortage of skilled talent. It is more important than ever for organizations to be able to attract, support and retain a talented workforce and to encourage more women to pursue and build vibrant careers in architecture, engineering and construction. Unfortunately, their attrition rate also remains high in these industries. Developing and retaining a skilled workforce includes identifying and addressing the specific needs of women in our industry. Man or Woman; Male or Female Brain, B-AdPW’s Rising Builders Summit will give you and your team the tools you need to excel as an Employer of Choice and a roadmap for individual continued career planning and success .

This unique Forum provides a venue to engage everyone from executives to those just beginning their careers with active, hands-on sessions and vibrant networking with the best and brightest in the A/E/C industry. In our usual B-AdPW Forum style, Keynotes become table participants and table participants become presenters, encouraging participants to assimilate what they are learning. Join local, state and national leaders and subject matter experts as we candidly explore and address the issues affecting women in our industry .

```html
<!DOCTYPE html>
<html lang="en">
<head>
<meta charset="utf-8">
<title>5th Annual Rising Builders Summit — Flyer</title>
<link href="https://fonts.googleapis.com/css2?family=Montserrat:wght@400;500;600;700&family=Oswald:wght@500;600&display=swap" rel="stylesheet">
<style>
  :root {
    --page-bg: #e9e9ea;
    --paper: #ffffff;
    --ink: #111111;
    --violet: #6a5cd0;
    --violet-deep: #4b3fb0;
    --navy: #0d0b3a;
    --floor-light: #dfe3f0;
    --text-light: #ffffff;
  }
  * { box-sizing: border-box; margin: 0; padding: 0; }
  html, body { width: 1200px; height: 1200px; overflow: hidden; background: var(--page-bg); }
  body { display: flex; align-items: center; justify-content: center; }

  .flyer {
    position: relative;
    width: 880px;
    height: 1130px;
    overflow: hidden;
    background: var(--paper);
    box-shadow: 0 10px 30px rgba(0,0,0,.12);
  }

  .hall-backdrop {
    position: absolute; inset: 0;
    background:
      linear-gradient(180deg,
        #ffffff 0%, #fbfbfd 48%,
        #1a1a22 49.2%, #2a2a38 49.8%,
        var(--floor-light) 50.5%, #c9c8ec 62%,
        var(--violet) 76%, var(--violet-deep) 84%,
        var(--navy) 100%);
  }

  .walker-photo {
    position: absolute; left: 365px; top: 360px;
    width: 200px; height: 460px;
    border-radius: 90px 90px 20px 20px;
    background: linear-gradient(180deg, #141414 0%, #1c1a2e 70%, #2a2460 100%);
  }

  .headline {
    position: absolute; left: 140px; top: 150px;
    font-family: "Montserrat", sans-serif;
    z-index: 2;
  }
  .headline-top { display: flex; align-items: flex-end; gap: 6px; }
  .ordinal-num { font-size: 62px; font-weight: 700; color: var(--ink); line-height: .8; }
  .ordinal-stack { display: flex; flex-direction: column; line-height: 1; }
  .ordinal-suffix { font-size: 20px; font-weight: 600; letter-spacing: 4px; color: var(--ink); }
  .annual { font-size: 32px; font-weight: 600; letter-spacing: 9px; color: var(--ink); }
  .annual .dot { color: var(--ink); margin: 0 4px; }
  .annual .rising { color: var(--violet); font-weight: 500; }
  .builders {
    font-size: 104px; font-weight: 500; letter-spacing: 12px;
    color: var(--violet); line-height: 1; margin-top: 6px;
  }
  .summit {
    text-align: right; margin-top: -4px; padding-right: 10px;
    font-size: 34px; font-weight: 700; letter-spacing: 10px; color: var(--ink);
  }

  .hashtag {
    position: absolute;
    font-family: "Oswald", sans-serif; font-weight: 600;
    font-size: 84px; color: var(--violet); line-height: 1;
  }
  .hashtag-left { right: 530px; top: 545px; }
  .hashtag-right { left: 580px; top: 480px; }

  .details {
    position: absolute; left: 0; right: 0; top: 840px;
    text-align: center; color: var(--text-light);
    font-family: "Oswald", sans-serif; font-weight: 500;
  }
  .event-date { font-size: 30px; letter-spacing: 1px; }
  .event-venue { font-size: 21px; letter-spacing: .5px; margin-top: 4px; }
  .details-rule { width: 560px; height: 3px; background: var(--text-light); margin: 12px auto 16px; }
  .organiser-intro {
    font-family: "Montserrat", sans-serif; font-weight: 600;
    font-size: 22px; letter-spacing: 7px;
  }

  .organisers {
    position: absolute; left: 0; right: 0; top: 1010px;
    display: flex; justify-content: center; gap: 70px;
  }
  .organiser { display: flex; align-items: center; gap: 12px; color: var(--text-light); font-family: "Montserrat", sans-serif; }
  .organiser-mark { width: 40px; height: 40px; border-radius: 50%; background: var(--violet); flex: none; }
  .organiser-name { font-size: 30px; font-weight: 500; line-height: 1; }
  .organiser-sub { font-size: 9px; font-weight: 500; margin-top: 4px; }
</style>
</head>
<body>
  <main class="flyer">
    <div class="hall-backdrop"></div>
    <div class="walker-photo" role="img" aria-label="Silhouette photo of a woman walking across a reflective hall floor, her figure filled with repeating #StandTall lettering"></div>

    <header class="headline">
      <div class="headline-top">
        <span class="ordinal-num">5</span>
        <span class="ordinal-stack">
          <span class="ordinal-suffix">TH</span>
          <span class="annual">ANNUAL<span class="dot">·</span><span class="rising">RISING</span></span>
        </span>
      </div>
      <div class="builders">BUILDERS</div>
      <div class="summit">SUMMIT</div>
    </header>

    <div class="hashtag hashtag-left">#STAND</div>
    <div class="hashtag hashtag-right">TALL</div>

    <section class="details">
      <p class="event-date">JANUARY 24, 2020</p>
      <p class="event-venue">HARBORVIEW LODGE HOTEL AND CONFERENCE CENTER, SAN MARCOS, TX</p>
      <div class="details-rule"></div>
      <p class="organiser-intro">THIS IS EVENT IS PUT TOGETHER BY</p>
    </section>

    <section class="organisers">
      <div class="organiser">
        <span class="organiser-mark"></span>
        <div>
          <p class="organiser-name">B-AdPW</p>
          <p class="organiser-sub">Bureau for Advancement in Public Works</p>
        </div>
      </div>
      <div class="organiser">
        <span class="organiser-mark"></span>
        <div>
          <p class="organiser-name">Ring of Merit</p>
          <p class="organiser-sub">Bureau for Advancement in Public Works</p>
        </div>
      </div>
    </section>
  </main>
</body>
</html>
```